Delegate Welcome sign

The Copperfield Lodge hotel in Pine Bush NY is welcoming delegations from many different countries during 2019. We want to make a welcome sign about 16:9 ratio about 4 feet high with raised letters. I have attached a background design that we liked and a template with the wording. As you will see I need help with it.

```html
<!DOCTYPE html>
<html lang="en">
<head>
<meta charset="utf-8">
<title>Copperfield Lodge – Delegate Welcome Sign</title>
<link href="https://fonts.googleapis.com/css2?family=Bebas+Neue&family=Kaushan+Script&display=swap" rel="stylesheet">
<style>
  :root {
    --page-bg: #d9d9d9;
    --wood-dark: #3a2414;
    --wood-mid: #5a3a22;
    --wood-light: #6e4a2c;
    --gold: #f2b51c;
    --gold-deep: #e89a1a;
    --hashtag: #e07a12;
    --ink-light: #ffffff;
    --wheat-light: #f3d9a0;
    --wheat-mid: #d9a955;
    --wheat-dark: #a8752a;
  }
  * { margin: 0; padding: 0; box-sizing: border-box; }
  html, body { width: 1200px; height: 927px; overflow: hidden; }
  body { background: var(--page-bg); position: relative; font-family: "Bebas Neue", sans-serif; }

  .welcome-sign {
    position: absolute; left: 82px; top: 157px; width: 1036px; height: 581px; overflow: hidden;
  }
  .wood-backdrop {
    position: absolute; inset: 0;
    background: radial-gradient(ellipse at 40% 40%, var(--wood-light) 0%, var(--wood-mid) 45%, var(--wood-dark) 100%);
  }
  .wheat-bundle {
    position: absolute; right: 0; top: 30px; width: 330px; height: 551px;
    background: radial-gradient(ellipse at 60% 35%, var(--wheat-light) 0%, var(--wheat-mid) 50%, rgba(168,117,42,0) 75%);
  }
  .sign-copy {
    position: absolute; left: 0; top: 0; width: 786px; height: 100%; text-align: center;
  }
  .brand { position: absolute; left: 0; right: 0; top: 118px; }
  .brand-mark {
    display: block; width: 14px; height: 14px; border-radius: 50%; background: var(--gold);
    margin: 0 auto 10px;
  }
  .brand-name { color: var(--gold); font-size: 40px; letter-spacing: 2px; line-height: 1; }
  .brand-place { color: var(--gold); font-size: 17px; letter-spacing: 3px; line-height: 1; margin-top: 4px; }
  .welcomes {
    position: absolute; left: 0; right: 0; top: 228px;
    font-family: "Kaushan Script", cursive; color: var(--gold); font-size: 62px; line-height: 1;
  }
  .headline {
    position: absolute; left: 0; right: 0; top: 315px;
    color: var(--ink-light); font-size: 60px; letter-spacing: 1px; line-height: 1;
  }
  .subline {
    position: absolute; left: 0; right: 0; top: 384px;
    color: var(--ink-light); font-size: 42px; letter-spacing: 0.5px; line-height: 1;
  }
  .divider {
    position: absolute; left: 98px; width: 590px; top: 464px; height: 2px;
    background: linear-gradient(90deg, var(--gold-deep), var(--gold), var(--gold-deep));
  }
  .hashtag {
    position: absolute; left: 0; right: 0; top: 530px;
    color: var(--hashtag); font-size: 22px; letter-spacing: 1px; line-height: 1;
  }
</style>
</head>
<body>
  <main class="welcome-sign">
    <div class="wood-backdrop" role="img" aria-label="Dark brown wood plank texture background"></div>
    <div class="wheat-bundle" role="img" aria-label="Illustration of a golden wheat sheaf"></div>
    <section class="sign-copy">
      <div class="brand">
        <span class="brand-mark"></span>
        <p class="brand-name">COPPERFIELD LODGE</p>
        <p class="brand-place">PINE BUSH, NY</p>
      </div>
      <p class="welcomes">Welcomes</p>
      <h1 class="headline">2019 INTERNATIONAL DELEGATES</h1>
      <p class="subline">TO THE HUDSON VALLEY IN NEW YORK</p>
      <div class="divider"></div>
      <p class="hashtag">#COPPERFIELDLODGEHOTEL</p>
    </section>
  </main>
</body>
</html>
```